Looking for a web design for event planning. Targeting the Wedding Industry, Corporate Meetings, Special Events, Fundraisers and other Celebratory Events
Home Page - name with pictures of various events- 3 buttons to go to
Wedding ( engagement parties, bridal showers, rehearsal dinners, welcome receptions and wedding receptions page
Corporate Meetings/Fundraisers page
Special Events/Celebratory Events
Updates

Target Market(s)

Brides, Wedding Planners, Corporate Event Planners, Destination Companies, Public

Industry/Entity Type

Event Planning

Contact Information for Business Card

name , phone number and email address
images of party images...wedding cake- balloons-party hat etc

Logo Text

Dana Ruth Okonkwo Event Design @ The Bayview Harbor Rowing Club

Number of Pages Required

4 page

Font styles to use
Decorative

Colors

Designer to choose colors to be used in the design.

Requirements
Must have
• Dana Ruth Okonkwo Event Design
• @ Bayview Harbor Rowing Club
• 415-555-0193
• droeventstudio@vesperlane.com
• back side of card - Image of Bayview Harbor Rowing Club
Nice to have
• fun and catchy party images
• wedding cake - diamond ring -balloons - party hat- flowers
• would like to see the images in white, gold and silver
Should not have
• photographic pictures

```html
<!DOCTYPE html>
<html lang="en">
<head>
<meta charset="utf-8">
<title>Dana Ruth Okonkwo Event — Home Page Concepts</title>
<link href="https://fonts.googleapis.com/css2?family=Mulish:wght@400;600;700;800&display=swap" rel="stylesheet">
<style>
:root{
  --gold:#c9a03a;
  --gold-soft:#e6c66b;
  --ink:#2b2b2b;
  --text:#555;
  --muted:#8a8a8a;
  --band:#eef1f5;
  --band-blue:#edf2f8;
  --footer:#2d2d2d;
  --white:#fff;
  --booked:#e04848;
  --available:#3aae5a;
}
*{margin:0;padding:0;box-sizing:border-box}
html,body{width:767px;height:1200px;overflow:hidden;background:#f7f7f7;font-family:'Mulish',sans-serif;color:var(--text)}
.stage{position:relative;width:959px;height:1500px;transform:scale(.8);transform-origin:0 0}
.page{position:absolute;top:45px;width:417px;background:var(--white);box-shadow:0 2px 10px rgba(0,0,0,.08);overflow:hidden}
.page--classic{left:45px;height:1413px}
.page--night{left:501px;height:1365px}
.a{position:absolute}
.ph{position:absolute}
.center{text-align:center}

/* top bar + nav */
.topbar{left:0;top:0;width:417px;height:11px;background:var(--gold);color:#fff;font-size:3.6px;display:flex;align-items:center;padding:0 55px;gap:8px}
.topbar .lang{margin-right:auto}
.nav{left:0;top:11px;width:417px;height:29px;background:#fff}
.brand{display:flex;align-items:center;gap:3px;font-size:5.4px;font-weight:800;line-height:5.6px;color:var(--ink);letter-spacing:.1px}
.brand .dot{width:8px;height:8px;border-radius:50%;border:1.2px solid var(--ink);flex:none}
.brand--light{color:#fff}
.brand--light .dot{border-color:#fff}
.menu{display:flex;gap:5px;font-size:3.7px;color:var(--ink)}
.menu--light{color:#fff}

/* hero */
.hero-title{font-size:14px;font-weight:800;color:#fff;letter-spacing:.1px}
.hero-sub{font-size:6px;font-weight:700;color:var(--gold-soft)}
.hero-perks{font-size:4.4px;color:#f3ead6;display:flex;gap:8px}
.hero-perks span::before{content:"";display:inline-block;width:3.5px;height:3.5px;border:.6px solid #fff;border-radius:50%;margin-right:1.5px;vertical-align:-.5px}
.btn-gold{background:var(--gold);color:#fff;font-size:4.4px;font-weight:800;display:flex;align-items:center;justify-content:center;letter-spacing:.2px}
.btn-white{background:#fff;color:var(--ink);font-size:5px;font-weight:800;display:flex;align-items:center;justify-content:center}
.play{width:16px;height:16px;border:1px solid #fff;border-radius:50%}
.play::after{content:"";position:absolute;left:6px;top:4.5px;border-left:5px solid #fff;border-top:3.2px solid transparent;border-bottom:3.2px solid transparent}

/* about */
.about{left:52px;width:140px;text-align:center}
.about .mark{width:9px;height:9px;border:1.2px solid var(--gold);border-radius:50%;margin:0 auto 3px}
.eyebrow{font-size:4.5px;font-weight:800;color:var(--ink);letter-spacing:.3px}
.about h2{font-size:8.4px;font-weight:800;color:var(--ink);line-height:10px;margin:5px 0 6px}
.about p{font-size:3.6px;line-height:4.6px;color:var(--text);margin:0 8px 4px}
.about .next{width:9px;height:9px;border-radius:50%;background:var(--gold);margin:7px auto 0;position:relative}
.about .next::after{content:"";position:absolute;left:3.3px;top:2.6px;border-left:2.8px solid #fff;border-top:1.9px solid transparent;border-bottom:1.9px solid transparent}

/* section titles */
.sec-title{font-size:8.4px;font-weight:800;color:var(--ink);line-height:11px;text-align:center;width:417px;left:0}
.rule{left:186px;width:44px;height:8px}
.rule::before,.rule::after{content:"";position:absolute;top:4px;width:14px;height:.6px;background:var(--muted)}
.rule::before{left:0}.rule::after{right:0}
.rule span{position:absolute;left:19px;top:1.5px;width:5px;height:5px;border:.8px solid var(--gold);border-radius:50%}
.swipe{width:16px;height:4px}
.swipe::before{content:"";position:absolute;left:1px;right:1px;top:1.8px;height:.6px;background:var(--gold)}
.swipe::after{content:"↔";position:absolute;left:0;top:-4px;font-size:8px;color:var(--gold);line-height:10px}

/* event cards */
.card{background:#fff;box-shadow:0 2px 6px rgba(0,0,0,.12);text-align:center}
.card .ph{left:0;top:0;width:100%;height:64px}
.card h3{position:absolute;top:68px;width:100%;font-size:5.6px;font-weight:800;color:var(--ink)}
.card p{position:absolute;top:76.5px;width:100%;font-size:3.4px;color:var(--muted)}
.card .more{position:absolute;top:84px;left:50%;transform:translateX(-50%);width:26px;height:6px;border:.6px solid var(--ink);font-size:2.9px;font-weight:700;color:var(--ink);line-height:5px}
.card--active{border-bottom:1.5px solid var(--gold)}
.card--active .more{border-color:var(--gold);color:var(--gold);width:30px;height:7px;line-height:6px}
.circle-arrow{width:10px;height:10px;border:.7px solid #bbb;border-radius:50%;color:#aaa;font-size:6px;line-height:8.5px;text-align:center}
.dots{left:188px;width:40px;height:1.4px;background:#ddd}
.dots::after{content:"";position:absolute;left:13px;width:9px;height:1.4px;background:var(--ink)}

/* portfolio */
.strip .ph{box-shadow:0 1px 2px rgba(0,0,0,.15)}
.read{font-size:3.8px}

/* we are */
.weare h2{font-size:11px;font-weight:700;color:var(--ink);line-height:13px;text-align:right}
.weare .tag{font-size:3.7px;color:var(--muted);text-align:right;line-height:4.6px;margin-top:4px}
.bullets{font-size:3.4px;color:var(--text);line-height:9.5px}
.bullets li{list-style:none}
.bullets li::before{content:"";display:inline-block;width:2.6px;height:2.6px;background:var(--ink);border-radius:50%;margin-right:4px;vertical-align:.3px}
.para{font-size:3.5px;line-height:4.6px;color:var(--text)}
.stats{display:flex;gap:12px}
.stat b{display:block;font-size:12px;font-weight:800;color:var(--gold);line-height:12px}
.stat span{font-size:3.6px;color:var(--ink)}

/* contact */
.field{background:#fff;border:.6px solid #e2e2e2;font-size:4.4px;color:#aaa;display:flex;align-items:center;padding-left:9px;gap:3px}
.field i{font-style:normal;color:#999}
.btn-cta{font-size:5px}
.tilt{box-shadow:0 3px 8px rgba(0,0,0,.25);border:3px solid #fff}

/* subscribe */
.sub-field{background:#fff;border:.6px solid #ddd;font-size:4px;color:#aaa;display:flex;align-items:center;padding-left:8px}
.btn-sub{font-size:4px}

/* calendar */
.cal{background:#fff;box-shadow:0 2px 8px rgba(0,0,0,.15)}
.cal-head{height:23px;background:var(--gold);color:#fff;padding:4px 7px}
.cal-head small{display:block;font-size:3.4px}
.cal-head b{font-size:6.4px;font-weight:700}
.cal-nav{position:absolute;top:29px;left:12px;right:12px;display:flex;justify-content:space-between;align-items:center;font-size:3.8px;color:var(--ink)}
.cal-nav b{font-weight:800}
.cal table{position:absolute;top:41px;left:8px;width:114px;border-collapse:collapse;font-size:3.8px;color:var(--ink);text-align:center}
.cal th{font-weight:800;height:12px}
.cal td{height:13.6px}
.cal td.out{color:#bbb}
.cal td span{display:inline-block;width:9px;height:9px;line-height:8px;border-radius:50%}
.cal td.bk span{border:.7px solid var(--booked)}
.cal td.av span{border:.7px solid var(--available)}
.cal-legend{position:absolute;bottom:5px;left:13px;font-size:3.6px;font-weight:800;display:flex;gap:10px}
.cal-legend .l-bk{color:var(--booked)}
.cal-legend .l-av{color:var(--available)}
.cal-legend span::before{content:"";display:inline-block;width:3.4px;height:3.4px;border:.6px solid currentColor;border-radius:50%;margin-right:2px;vertical-align:-.4px}

/* footer */
.footer{left:0;width:417px;background:var(--footer);color:#cfcfcf}
.footer .about-txt{font-size:3.7px;line-height:4.7px;width:90px;color:#cfcfcf}
.footer h4{font-size:4.6px;font-weight:800;color:#fff}
.footer ul{font-size:3.5px;line-height:8.8px;list-style:none}
.footer ul li::before{content:"› ";color:var(--gold)}
.footer .contact{font-size:3.8px;line-height:9px;color:#fff}
.footer .copy{font-size:3.5px;color:#cfcfcf}
</style>
</head>
<body>
<div class="stage">

<!-- ================= CLASSIC PAGE ================= -->
<section class="page page--classic">
  <div class="a topbar"><span class="lang">Lan: Eng ⌄</span><span>◷ working hours: 9-10pm</span><span>|</span><span>✉ okonkwoevent@vesperlane.com</span><span>|</span><span>✆ 415-555-0193</span></div>
  <div class="a nav"></div>
  <div class="a brand" style="left:54px;top:20px"><span class="dot"></span><span>DANA RUTH<br>OKONKWO EVENT</span></div>
  <nav class="a menu" style="left:138px;top:26px"><span>Home</span><span>About us</span><span>Wedding</span><span>Corporate Meetings</span><span>Fundraisers</span><span>Special Events</span><span>Celebratory Events</span><span>Contact us</span></nav>

  <div class="ph" role="img" aria-label="Banquet hall set for a reception with round tables and warm uplighting" style="left:0;top:40px;width:417px;height:170px;background:linear-gradient(135deg,#8a6a3e 0%,#5c4427 45%,#3a2a18 75%,#6b5231 100%)"></div>
  <svg class="a" style="left:0;top:40px" width="417" height="170" viewBox="0 0 417 170"><path d="M0,150 C20,162 50,168 92,165 C200,158 330,132 417,108 L417,170 L0,170Z" fill="#fff"/></svg>
  <div class="a hero-title" style="left:53px;top:85px">Dana Ruth Okonkwo Event</div>
  <div class="a hero-sub" style="left:53px;top:103px">Wedding, Corporate Meetings, Fundraisers</div>
  <div class="a hero-perks" style="left:53px;top:117px"><span>Low Cost</span><span>Best Service</span></div>
  <div class="a btn-gold" style="left:53px;top:133px;width:65px;height:13px">VIEW OUR EVENTS</div>

  <div class="a about" style="top:250px">
    <div class="mark"></div>
    <div class="eyebrow">ABOUT US</div>
    <h2>Sed ut perspiciatis unde omnis iste natus error sit voluptatem accusant</h2>
    <p>Sed ut perspiciatis unde omnis iste natus error sit voluptatem accusantium doloremque laudantium, totam rem aperiam sed quia non numquam eius modi tempora .</p>
    <p>At vero eos et accusamus et iusto odio dignissimos ducimus qui blanditiis praesentium voluptatum deleniti atque corrupti quos dolores et quas molest ias excepturi sint occaecati cupiditate est</p>
    <div class="next"></div>
  </div>
  <div class="ph" role="img" aria-label="Table centrepiece of red roses, pine cones and a lit candle" style="left:208px;top:234px;width:155px;height:163px;background:radial-gradient(circle at 50% 35%,#d88a3a 0%,#8c1e22 35%,#5a1216 65%,#2b1b12 100%)"></div>

  <div class="a sec-title" style="top:435px">Okonkwo Events</div>
  <div class="a circle-arrow" style="left:34px;top:495px">‹</div>
  <div class="a circle-arrow" style="left:371px;top:495px">›</div>
  <div class="a card" style="left:56px;top:454px;width:94px;height:95px">
    <div class="ph" role="img" aria-label="Bride and groom at their wedding" style="background:linear-gradient(180deg,#b8a79a,#e9e3de 60%,#f7f4f1)"></div>
    <h3>Wedding</h3><p>Dolores eiusis molestit excepturi</p><div class="more">READ MORE</div>
  </div>
  <div class="a card card--active" style="left:159px;top:454px;width:98px;height:103px">
    <div class="ph" role="img" aria-label="Corporate dinner in a crowded hall" style="background:linear-gradient(180deg,#6b5a48,#3a2d22 60%,#2a2018)"></div>
    <h3>Corporate</h3><p>Dolores eiusis molestit excepturi</p><div class="more">READ MORE</div>
  </div>
  <div class="a card" style="left:263px;top:454px;width:99px;height:95px">
    <div class="ph" role="img" aria-label="Guests seated at a celebratory banquet" style="background:linear-gradient(180deg,#8a7760,#5a4a3a 60%,#3a3028)"></div>
    <h3>Celebratory Events</h3><p>Dolores eiusis molestit excepturi</p><div class="more">READ MORE</div>
  </div>
  <div class="a dots" style="top:577px"></div>

  <div class="a" style="left:0;top:612px;width:417px;height:390px;background:var(--band)"></div>
  <svg class="a" style="left:0;top:780px" width="417" height="222" viewBox="0 0 417 222"><path d="M0,40 L20,28 L45,44 L60,30 L95,48 L130,22 L170,40 L210,18 L250,36 L290,14 L330,34 L370,20 L417,38 L417,222 L0,222Z" fill="#f6f8fa"/><rect x="55" y="60" width="310" height="162" fill="#fff"/></svg>
  <div class="a sec-title" style="top:640px">Portfolio<br>Our Latest Events</div>
  <div class="a swipe" style="left:322px;top:647px"></div>
  <div class="a rule" style="top:667px"><span></span></div>
  <div class="strip">
    <div class="ph" role="img" aria-label="Christmas tree at an evening party" style="left:0;top:701px;width:43px;height:71px;background:linear-gradient(160deg,#1f3a5a,#2e5a3a 60%,#7a5a3a)"></div>
    <div class="ph" role="img" aria-label="Decorated tree in a reception room" style="left:44px;top:701px;width:59px;height:71px;background:linear-gradient(160deg,#3a4a3a,#6b5a3a 60%,#a08050)"></div>
    <div class="ph" role="img" aria-label="Guests mingling at a holiday gathering" style="left:105px;top:701px;width:61px;height:71px;background:linear-gradient(160deg,#a89a8a,#6b5a4a 60%,#3a3028)"></div>
    <div class="ph" role="img" aria-label="Tiered wedding cake with sugar roses" style="left:168px;top:689px;width:79px;height:95px;background:radial-gradient(circle at 50% 45%,#f3d8c0 0%,#e8a070 40%,#b86a3a 100%)"></div>
    <div class="ph" role="img" aria-label="Dessert buffet table" style="left:250px;top:701px;width:59px;height:71px;background:linear-gradient(160deg,#e8e0d8,#8a5a4a 60%,#3a2a22)"></div>
    <div class="ph" role="img" aria-label="Candlelit table setting" style="left:311px;top:701px;width:60px;height:71px;background:linear-gradient(160deg,#2a2622,#6a5a4a 55%,#c8b8a0)"></div>
    <div class="ph" role="img" aria-label="Banquet tables with red linens" style="left:372px;top:701px;width:45px;height:71px;background:linear-gradient(160deg,#4a3a30,#8a3a34 60%,#5a2a26)"></div>
  </div>
  <div class="a btn-gold read" style="left:191px;top:803px;width:34px;height:9px">READ MORE</div>

  <div class="a weare" style="left:60px;top:898px;width:96px"><h2>We Are<br>Okonkwo Events</h2><div class="tag">An honest and best results<br>event management</div></div>
  <ul class="a bullets" style="left:195px;top:899px"><li>At vero eos et accusamus et iusto</li><li>At vero eos et accusamus et iusto</li><li>ducimus qui blanditiis praesentium volupt</li></ul>
  <p class="a para" style="left:190px;top:934px;width:175px">Nam libero tempore, cum soluta nobis est eligendi optio cumque nihil impedit quo minus id quod maxime placeat facere possimus, omnis voluptas assumenda est, omnis dolor repellendus. Temporibus autem quibusdam molestiae non recusandae.</p>
  <div class="a stats" style="left:188px;top:967px"><div class="stat"><b>1600</b><span>Events</span></div><div class="stat"><b>1200</b><span>Happy Clients</span></div><div class="stat"><b>200</b><span>Best Ever</span></div><div class="stat"><b>400</b><span>Creative Events</span></div></div>

  <div class="a" style="left:0;top:1057px;width:417px;height:98px;background:var(--band)"></div>
  <div class="a field" style="left:65px;top:1073px;width:123px;height:16px"><i>👤</i>Name</div>
  <div class="a field" style="left:65px;top:1097px;width:123px;height:16px"><i>✆</i>Phone No</div>
  <div class="a btn-gold btn-cta" style="left:65px;top:1121px;width:123px;height:18px">CONTACT US NOW</div>
  <div class="ph tilt" role="img" aria-label="Newlywed couple celebrating outdoors" style="left:232px;top:1037px;width:88px;height:138px;transform:rotate(4deg);background:linear-gradient(170deg,#cfd6c8,#e8e4de 45%,#3a3a3a 80%)"></div>

  <div class="a sec-title" style="top:1204px">Want To Get Started With Us</div>
  <p class="a para center" style="left:113px;top:1224px;width:190px">Nam libero tempore, cum soluta nobis est eligendi optio cumque nihil impedit quo minus id quod maxime placeat facere possimus, omnis voluptas assumenda.</p>
  <div class="a sub-field" style="left:135px;top:1253px;width:107px;height:14px">✉ Enter Email</div>
  <div class="a btn-gold btn-sub" style="left:242px;top:1253px;width:40px;height:14px">SUBSCRIBE</div>

  <footer class="a footer" style="top:1305px;height:108px">
    <div class="a brand brand--light" style="left:59px;top:25px"><span class="dot"></span><span>DANA RUTH<br>OKONKWO EVENT</span></div>
    <p class="a about-txt" style="left:57px;top:46px">Nam libero tempore, cum soluta nobis est eligendi optio cumque nihil impedit quorns mus id quod maxime placeat facere rerum necessitatibus saepe eveniet.</p>
    <h4 class="a" style="left:173px;top:22px">Quick Links</h4>
    <ul class="a" style="left:173px;top:31px"><li>Home</li><li>About us</li><li>Wedding</li><li>Corporate Meetings</li></ul>
    <ul class="a" style="left:233px;top:31px"><li>Fundraisers</li><li>Special Events</li><li>Celebratory Events</li><li>Contact us</li></ul>
    <h4 class="a" style="left:295px;top:22px">Contact Us</h4>
    <div class="a contact" style="left:295px;top:31px">✆ 415-555-0193<br>✉ okonkwoevent@vesperlane.com</div>
    <div class="a copy" style="left:170px;top:90px">Copyright © 2019. All Rights Reserved.</div>
  </footer>
</section>

<!-- ================= NIGHT PAGE ================= -->
<section class="page page--night">
  <div class="ph" role="img" aria-label="Evening reception hall with blue uplighting and long dining tables" style="left:0;top:0;width:417px;height:205px;background:radial-gradient(ellipse at 85% 40%,#3ab0d8 0%,#1f5a8a 30%,#15304e 60%,#0f1c2e 100%)"></div>
  <div class="a" style="left:0;top:0;width:417px;height:205px;background:rgba(10,20,35,.25)"></div>
  <div class="a brand brand--light" style="left:54px;top:17px"><span class="dot"></span><span>DANA RUTH<br>OKONKWO EVENT</span></div>
  <nav class="a menu menu--light" style="left:140px;top:24px"><span>Home</span><span>About us</span><span>Wedding</span><span>Corporate Meetings</span><span>Fundraisers</span><span>Special Events</span><span>Celebratory Events</span><span>Contact us</span></nav>
  <div class="a play" style="left:200px;top:75px"></div>
  <div class="a hero-title center" style="left:0;top:99px;width:417px">Dana Ruth Okonkwo Event</div>
  <div class="a hero-sub center" style="left:0;top:120px;width:417px;color:#fff">Wedding, Corporate Meetings, Fundraisers</div>
  <div class="a btn-white" style="left:160px;top:141px;width:96px;height:14px">REQUEST FREE CALL</div>

  <div class="a about" style="top:250px">
    <div class="mark"></div>
    <div class="eyebrow">ABOUT US</div>
    <h2>Sed ut perspiciatis unde omnis iste natus error sit voluptatem accusant</h2>
    <p>Sed ut perspiciatis unde omnis iste natus error sit voluptatem accusantium doloremque laudantium, totam rem aperiam sed quia non numquam eius modi tempora .</p>
    <p>At vero eos et accusamus et iusto odio dignissimos ducimus qui blanditiis praesentium voluptatum deleniti atque corrupti quos dolores et quas molest ias excepturi sint occaecati cupiditate est</p>
    <div class="next"></div>
  </div>

  <div class="a cal" style="left:222px;top:247px;width:130px;height:146px">
    <div class="cal-head"><small>2019</small><b>THU, JAN 19</b></div>
    <div class="cal-nav"><span>‹ DEC</span><b>JAN 2019</b><span>FEB ›</span></div>
    <table>
      <tr><th>S</th><th>M</th><th>T</th><th>W</th><th>T</th><th>F</th><th>S</th></tr>
      <tr><td class="out">30</td><td class="out">31</td><td>1</td><td>2</td><td class="bk"><span>3</span></td><td>4</td><td class="av"><span>5</span></td></tr>
      <tr><td>6</td><td>7</td><td class="av"><span>8</span></td><td>9</td><td>10</td><td>11</td><td>12</td></tr>
      <tr><td>13</td><td>14</td><td>15</td><td>16</td><td class="av"><span>17</span></td><td>18</td><td class="av"><span>19</span></td></tr>
      <tr><td>20</td><td class="av"><span>21</span></td><td>22</td><td>23</td><td>24</td><td>25</td><td>26</td></tr>
      <tr><td>27</td><td>28</td><td>29</td><td class="bk"><span>30</span></td><td>31</td><td class="out av"><span>1</span></td><td class="out">2</td></tr>
    </table>
    <div class="cal-legend"><span class="l-bk">BOOKED</span><span class="l-av">AVAILABLE</span></div>
  </div>

  <div class="a sec-title" style="top:435px">Okonkwo Events</div>
  <div class="a circle-arrow" style="left:34px;top:495px">‹</div>
  <div class="a circle-arrow" style="left:371px;top:495px">›</div>
  <div class="a card" style="left:56px;top:454px;width:94px;height:95px">
    <div class="ph" role="img" aria-label="Bride and groom in a formal hall" style="background:linear-gradient(180deg,#e8e6e2,#8a8580 55%,#2a2826)"></div>
    <h3>Wedding</h3><p>Dolores eiusis molestit excepturi</p><div class="more">READ MORE</div>
  </div>
  <div class="a card card--active" style="left:159px;top:454px;width:98px;height:103px">
    <div class="ph" role="img" aria-label="Corporate holiday dinner with a decorated tree" style="background:linear-gradient(180deg,#c8b8a0,#7a5040 55%,#3a2420)"></div>
    <h3>Corporate</h3><p>Dolores eiusis molestit excepturi</p><div class="more">READ MORE</div>
  </div>
  <div class="a card" style="left:263px;top:454px;width:99px;height:95px">
    <div class="ph" role="img" aria-label="Balloon arch in purple party lighting" style="background:radial-gradient(circle at 50% 40%,#e8d8f0 0%,#a040c0 40%,#5a1a8a 100%)"></div>
    <h3>Celebratory Events</h3><p>Dolores eiusis molestit excepturi</p><div class="more">READ MORE</div>
  </div>
  <div class="a dots" style="top:577px"></div>

  <div class="a" style="left:0;top:627px;width:417px;height:100px;background:var(--band)"></div>
  <div class="ph tilt" role="img" aria-label="Table centrepiece of red roses and a lit candle" style="left:83px;top:610px;width:91px;height:140px;transform:rotate(-5deg);background:radial-gradient(circle at 50% 40%,#d88a3a 0%,#8c1e22 35%,#5a1216 65%,#2b1b12 100%)"></div>
  <div class="a field" style="left:211px;top:645px;width:123px;height:16px"><i>👤</i>Name</div>
  <div class="a field" style="left:211px;top:669px;width:123px;height:16px"><i>✆</i>Phone No</div>
  <div class="a btn-gold btn-cta" style="left:211px;top:694px;width:123px;height:18px">CONTACT US NOW</div>

  <div class="a weare" style="left:60px;top:786px;width:96px"><h2>We Are<br>Okonkwo Events</h2><div class="tag">An honest and best results<br>event management</div></div>
  <ul class="a bullets" style="left:195px;top:771px"><li>At vero eos et accusamus et iusto</li><li>At vero eos et accusamus et iusto</li><li>ducimus qui blanditiis praesentium volupt</li></ul>
  <p class="a para" style="left:190px;top:805px;width:175px">Nam libero tempore, cum soluta nobis est eligendi optio cumque nihil impedit quo minus id quod maxime placeat facere possimus, omnis voluptas assumenda est, omnis dolor repellendus. Temporibus autem quibusdam molestiae non recusandae.</p>
  <div class="a stats" style="left:188px;top:837px"><div class="stat"><b>1600</b><span>Events</span></div><div class="stat"><b>1200</b><span>Happy Clients</span></div><div class="stat"><b>200</b><span>Best Ever</span></div><div class="stat"><b>400</b><span>Creative Events</span></div></div>

  <div class="a" style="left:0;top:893px;width:417px;height:120px;background:var(--band-blue)"></div>
  <div class="a sec-title" style="top:922px">Want To Get Started With Us</div>
  <p class="a para center" style="left:113px;top:942px;width:190px">Nam libero tempore, cum soluta nobis est eligendi optio cumque nihil impedit quo minus id quod maxime placeat facere possimus, omnis voluptas assumenda.</p>
  <div class="a sub-field" style="left:134px;top:970px;width:107px;height:14px">✉ Enter Email</div>
  <div class="a btn-gold btn-sub" style="left:241px;top:970px;width:40px;height:14px">SUBSCRIBE</div>

  <div class="a sec-title" style="top:1049px">Portfolio<br>Our Latest Events</div>
  <div class="a swipe" style="left:320px;top:1056px"></div>
  <div class="a rule" style="top:1077px"><span></span></div>
  <div class="strip">
    <div class="ph" role="img" aria-label="Buffet table in a warmly lit hall" style="left:0;top:1110px;width:41px;height:71px;background:linear-gradient(160deg,#e8d8b8,#8a6a40 60%,#3a2a1a)"></div>
    <div class="ph" role="img" aria-label="Dessert display with name cards" style="left:44px;top:1110px;width:60px;height:71px;background:linear-gradient(160deg,#f0ece6,#b8a890 55%,#5a4a3a)"></div>
    <div class="ph" role="img" aria-label="Round tables dressed in red" style="left:106px;top:1110px;width:60px;height:71px;background:linear-gradient(160deg,#3a2a2a,#9a2a2a 55%,#4a1a1a)"></div>
    <div class="ph" role="img" aria-label="Couple on a candlelit beach at dusk" style="left:169px;top:1098px;width:78px;height:95px;background:linear-gradient(180deg,#5a6aa0 0%,#c08ab0 45%,#e8c8a0 75%,#b8906a 100%)"></div>
    <div class="ph" role="img" aria-label="Guests in a white-draped reception" style="left:250px;top:1110px;width:59px;height:71px;background:linear-gradient(160deg,#e0ddd8,#8a8580 55%,#3a3836)"></div>
    <div class="ph" role="img" aria-label="Speaker addressing a dinner party" style="left:312px;top:1110px;width:59px;height:71px;background:linear-gradient(160deg,#5a4a3a,#2a2420 55%,#6a5a48)"></div>
    <div class="ph" role="img" aria-label="Long banquet table under string lights" style="left:373px;top:1110px;width:44px;height:71px;background:linear-gradient(160deg,#d8dcd8,#7a8078 55%,#3a3e3a)"></div>
  </div>
  <div class="a btn-gold read" style="left:190px;top:1211px;width:36px;height:11px">READ MORE</div>

  <footer class="a footer" style="top:1251px;height:114px">
    <div class="a brand brand--light" style="left:59px;top:26px"><span class="dot"></span><span>DANA RUTH<br>OKONKWO EVENT</span></div>
    <p class="a about-txt" style="left:57px;top:47px">Nam libero tempore, cum soluta nobis est eligendi optio cumque nihil impedit quorns mus id quod maxime placeat facere rerum necessitatibus saepe eveniet.</p>
    <h4 class="a" style="left:173px;top:23px">Quick Links</h4>
    <ul class="a" style="left:173px;top:32px"><li>Home</li><li>About us</li><li>Wedding</li><li>Corporate Meetings</li></ul>
    <ul class="a" style="left:233px;top:32px"><li>Fundraisers</li><li>Special Events</li><li>Celebratory Events</li><li>Contact us</li></ul>
    <h4 class="a" style="left:295px;top:23px">Contact Us</h4>
    <div class="a contact" style="left:295px;top:32px">✆ 415-555-0193<br>✉ okonkwoevent@vesperlane.com</div>
    <div class="a copy" style="left:170px;top:92px">Copyright © 2019. All Rights Reserved.</div>
  </footer>
</section>

</div>
</body>
</html>
```